Insurance company needs a business card design

We need a business card design for a Massachusetts-based insurance company Cielora Insurance, LLC. We provide auto insurance to Hispanic (Spanish- or Portuguese-speaking) immigrants in the United States. We will give these business cards to auto dealers where such customers typically go to purchase vehicles. We will provide a solution to the dealers to provide easy insurance to the customers buying cars at their dealerships. Cielora is the Spanish word for protection.
Contact Information for Business Card
Name, Designation, Company Name, Address, Phone Number, Email, Website
Look and feel
Each slider illustrates characteristics of the customer's brand and the style your logo design should communicate.

```html
<!DOCTYPE html>
<html lang="en">
<head>
<meta charset="utf-8">
<title>Cielora Insurance – Business Card</title>
<link href="https://fonts.googleapis.com/css2?family=Montserrat:wght@500;700;800&family=Arimo:wght@400&display=swap" rel="stylesheet">
<style>
  :root {
    --navy: #0a4a7c;
    --navy-deep: #063a63;
    --orange: #e07a1f;
    --ink: #2b2b2b;
    --paper: #ffffff;
    --backdrop: #e6e6e4;
  }
  * { box-sizing: border-box; margin: 0; padding: 0; }
  html, body { width: 1200px; height: 801px; overflow: hidden; }
  body {
    background: var(--backdrop);
    display: flex;
    align-items: center;
    justify-content: center;
    gap: 50px;
    font-family: "Arimo", Arial, sans-serif;
  }
  .card {
    width: 525px;
    height: 300px;
    position: relative;
    border-bottom: 3px solid var(--orange);
    box-shadow: 0 6px 18px rgba(0,0,0,.18);
  }
  /* Front */
  .card-front {
    background: var(--paper);
    display: flex;
    flex-direction: column;
    align-items: center;
    padding-top: 62px;
  }
  .brand-name {
    font-family: "Montserrat", sans-serif;
    font-weight: 800;
    color: var(--navy);
    font-size: 30px;
    letter-spacing: 1px;
    line-height: 1;
    display: flex;
    align-items: center;
    gap: 10px;
  }
  .brand-mark {
    width: 14px; height: 14px;
    background: var(--orange);
  }
  .details {
    margin-top: 36px;
    display: flex;
    align-items: center;
  }
  .person { text-align: right; padding-right: 22px; }
  .person-name {
    font-family: "Montserrat", sans-serif;
    font-weight: 700;
    font-size: 17px;
    color: var(--orange);
    letter-spacing: .5px;
  }
  .person-title { font-size: 14px; color: var(--ink); margin-top: 3px; }
  .divider { width: 1px; height: 62px; background: var(--ink); }
  .contacts { list-style: none; padding-left: 22px; }
  .contacts li {
    display: flex; align-items: center; gap: 8px;
    font-size: 13px; color: var(--ink); line-height: 21px;
  }
  .contacts svg { width: 12px; height: 12px; flex: none; }
  .address { margin-top: 28px; font-size: 13px; color: var(--ink); }
  /* Back */
  .card-back {
    background: linear-gradient(160deg, var(--navy) 0%, var(--navy-deep) 100%);
    display: flex;
    align-items: flex-end;
    justify-content: flex-end;
    padding: 0 36px 60px 0;
  }
  .card-back .brand-name { color: #ffffff; font-size: 32px; }
</style>
</head>
<body>
  <section class="card card-front" aria-label="Business card front">
    <div class="brand-name"><span class="brand-mark"></span>CIELORA INSURANCE</div>
    <div class="details">
      <div class="person">
        <div class="person-name">MARCOS DELVANE</div>
        <div class="person-title">Manager</div>
      </div>
      <div class="divider"></div>
      <ul class="contacts">
        <li>
          <svg viewBox="0 0 12 12"><path d="M2.5 1h2l1 2.5-1.3 1a6 6 0 0 0 3.3 3.3l1-1.3 2.5 1v2a1 1 0 0 1-1 1A9 9 0 0 1 1.5 2a1 1 0 0 1 1-1z" fill="var(--orange)"/></svg>
          555-014-2100
        </li>
        <li>
          <svg viewBox="0 0 12 12"><rect x="1" y="2.5" width="10" height="7" fill="none" stroke="var(--orange)" stroke-width="1.2"/><path d="M1 3l5 3.5L11 3" fill="none" stroke="var(--orange)" stroke-width="1.2"/></svg>
          hello@cieloramail.com
        </li>
        <li>
          <svg viewBox="0 0 12 12"><circle cx="6" cy="6" r="5" fill="none" stroke="var(--orange)" stroke-width="1.2"/><ellipse cx="6" cy="6" rx="2.2" ry="5" fill="none" stroke="var(--orange)" stroke-width="1"/><path d="M1 6h10" stroke="var(--orange)" stroke-width="1"/></svg>
          www.cielorainsure.com
        </li>
      </ul>
    </div>
    <p class="address">Your address, city, state, ZIP 0000</p>
  </section>

  <section class="card card-back" aria-label="Business card back">
    <div class="brand-name">CIELORA INSURANCE</div>
  </section>
</body>
</html>
```